Create Social Media design templates for Online-Education-Startup

We are an online platform for pupils who provide group courses and on demand individual tutroing lessons. Our core values are personalisation, family and success. We need a holistic social media design concept which includes nine possible layouts for Instagram posts which reflect our values and promote not only our offerings and special deals but also support in building our brand image (for example: telling company history, daily news, funny facts, getting to know the team etc.).
Additionally, we need design elements for our Streamly channel:
-Videocover
-Cover Image for the channel

Our main colour is orange (RGB-Code: 255;105;31) and additional colours white, black, and grey. For the reference have a look at our website: www.lernfolix.de.

Target Market(s)

We want to attract customers to our online tutoring courses and build a brand.

Industry/Entity Type

Education / Tutoring

Font styles to use
Sans Serif

Requirements
Must have
• Familiarize yourself with the style of our website. The designs should fit as well as possible.

```html
<!DOCTYPE html>
<html lang="en">
<head>
<meta charset="utf-8">
<title>Lernwerk Bildungsinstitut – Channel Page and Video Cover</title>
<link rel="stylesheet" href="https://fonts.googleapis.com/css2?family=Poppins:wght@400;500;600;700&family=Roboto:wght@400;500;700&family=Oswald:wght@500&display=swap">
<style>
  :root {
    --orange: rgb(255, 105, 31);
    --orange-soft: rgba(232, 140, 100, 0.82);
    --white: #ffffff;
    --black: #111111;
    --text-grey: #777777;
    --grey-light: #d0d0d0;
    --grey-band: #f1f1f1;
    --grey-stage: #979797;
    --grey-line: #bdbdbd;
    --rule: #e3e3e3;
    --thumb: #2b2b2d;
    --accent-violet: #6a5acd;
    --red: #e0201e;
    --photo-dark: #3b2a22;
    --photo-mid: #6e4f3c;
    --photo-light: #c9a98e;
  }
  * { margin: 0; padding: 0; box-sizing: border-box; }
  html, body { width: 928px; height: 1200px; overflow: hidden; }
  body {
    position: relative;
    background: var(--white);
    font-family: "Poppins", sans-serif;
    color: var(--black);
  }
  .abs { position: absolute; }

  /* ---------- Channel page ---------- */
  .channel-page { position: absolute; left: 0; top: 0; width: 928px; height: 613px; background: var(--white); }

  .topbar { position: absolute; left: 0; top: 0; width: 928px; height: 26px; border-bottom: 2px solid var(--rule); font-family: "Roboto", sans-serif; }
  .topbar__menu { left: 128px; top: 8px; width: 9px; height: 7px; border-top: 1px solid #999; border-bottom: 1px solid #999; }
  .topbar__menu::after { content: ""; position: absolute; left: 0; top: 2px; width: 9px; height: 1px; background: #999; }
  .topbar__platform { left: 150px; top: 5px; font-size: 10px; font-weight: 700; color: #222; letter-spacing: -0.3px; }
  .topbar__search { left: 240px; top: 4px; width: 289px; height: 14px; border: 1px solid #d6d6d6; background: var(--white); }
  .topbar__search-btn { right: 0; top: 0; width: 34px; height: 12px; background: #f4f4f4; border-left: 1px solid #d6d6d6; }
  .topbar__icons { left: 720px; top: 3px; }

  .channel-art { position: absolute; left: 0; top: 27px; width: 928px; height: 158px; background: var(--white); }
  .channel-art__values {
    position: absolute; left: 218px; top: 53px; width: 160px;
    text-align: center; font-size: 13px; font-weight: 500; line-height: 1.34; letter-spacing: 0.3px;
    white-space: nowrap;
  }

  .brand { position: absolute; display: flex; align-items: center; }
  .brand__mark { flex: none; border-style: solid; border-color: var(--orange); border-radius: 50%; }
  .brand__name { line-height: 1.2; color: var(--black); }
  .brand__name strong { display: block; font-weight: 600; }
  .brand__name span { display: block; font-weight: 400; }

  .channel-art .brand { left: 552px; top: 55px; gap: 7px; }
  .channel-art .brand__mark { width: 52px; height: 46px; border-width: 3px; }
  .channel-art .brand__name { font-size: 14px; }

  .channel-head { position: absolute; left: 0; top: 185px; width: 928px; height: 76px; background: var(--grey-band); font-family: "Roboto", sans-serif; }
  .channel-head__avatar { left: 127px; top: 11px; width: 40px; height: 40px; border-radius: 50%; background: var(--white); }
  .channel-head__name { left: 181px; top: 16px; font-family: "Poppins", sans-serif; font-size: 11px; font-weight: 500; color: #222; }
  .channel-head__subs { left: 181px; top: 32px; font-size: 6.5px; color: var(--text-grey); }
  .channel-head__subscribe {
    left: 698px; top: 20px; width: 94px; height: 20px; background: var(--red); color: var(--white);
    font-size: 6.5px; font-weight: 500; letter-spacing: 0.3px; display: flex; align-items: center; justify-content: center;
  }
  .tabs { left: 127px; top: 58px; display: flex; font-size: 6.5px; color: var(--text-grey); letter-spacing: 0.2px; }
  .tabs__item { position: absolute; top: 0; white-space: nowrap; }
  .tabs__item--active { color: #222; font-weight: 500; }
  .tabs__underline { left: 127px; top: 73px; width: 54px; height: 2px; background: #555; }

  .featured-cover { left: 127px; top: 273px; width: 312px; height: 176px; overflow: hidden; }
  .featured-cover .video-cover { transform: scale(0.3764); transform-origin: 0 0; }

  .featured-info { left: 461px; top: 277px; width: 262px; font-family: "Roboto", sans-serif; }
  .featured-info__title { font-size: 8.5px; font-weight: 500; color: #222; }
  .featured-info__meta { margin-top: 2px; font-size: 4.8px; color: var(--text-grey); }
  .featured-info__body { margin-top: 12px; font-size: 5.4px; line-height: 11px; color: #666; }
  .featured-info__rule { margin: 8px 0 14px; border-top: 1px dashed #c8c8c8; width: 258px; }

  .section-rule { left: 127px; top: 462px; width: 666px; height: 1px; background: var(--rule); }
  .uploads-label { left: 127px; top: 475px; font-family: "Roboto", sans-serif; font-size: 7px; font-weight: 500; color: #222; }
  .uploads-play { left: 180px; top: 476px; font-family: "Roboto", sans-serif; font-size: 6px; color: var(--text-grey); }

  .uploads { left: 127px; top: 498px; display: flex; gap: 2px; font-family: "Roboto", sans-serif; }
  .upload { width: 109px; }
  .upload__thumb { position: relative; height: 61px; background: var(--thumb); }
  .upload__badge { position: absolute; right: 5px; top: 5px; width: 7px; height: 7px; border: 1px solid var(--accent-violet); border-radius: 50%; }
  .upload__highlight { position: absolute; left: 5px; top: 40px; font-family: "Oswald", sans-serif; font-style: italic; font-size: 8px; color: var(--white); letter-spacing: -0.2px; }
  .upload__sub { position: absolute; left: 5px; top: 51px; width: 40px; height: 2px; background: var(--accent-violet); }
  .upload__title { margin-top: 6px; font-size: 6px; font-weight: 500; color: #222; white-space: nowrap; }
  .upload__meta { margin-top: 2px; font-size: 4.6px; color: var(--text-grey); white-space: nowrap; }

  /* ---------- Video cover ---------- */
  .stage { position: absolute; left: 0; top: 613px; width: 928px; height: 587px; background: var(--grey-stage); }
  .stage .video-cover { position: absolute; left: 50px; top: 63px; }
  .video-cover { width: 829px; height: 466px; background: var(--grey-light); overflow: hidden; position: relative; }
  .video-cover__art { position: absolute; left: 0; top: 0; }
  .video-cover .brand { left: 53px; top: 33px; gap: 13px; }
  .video-cover .brand__mark { width: 96px; height: 79px; border-width: 5px; }
  .video-cover .brand__name { font-size: 26px; }
  .video-cover .brand__name span { font-size: 24px; }
  .video-cover__tagline {
    position: absolute; left: 20px; top: 220px; width: 650px; height: 83px;
    padding: 13px 8px 0 8px; background: var(--orange-soft); border-radius: 8px;
    color: var(--white); font-size: 21.5px; font-weight: 600; line-height: 1.27; white-space: nowrap;
  }
  .video-cover__stripe { position: absolute; left: 0; width: 100%; background: var(--orange); }
  .video-cover__stripe--upper { top: 426px; height: 8px; }
  .video-cover__stripe--lower { top: 440px; height: 6px; }
</style>
</head>
<body>

<section class="channel-page">
  <header class="topbar">
    <div class="abs topbar__menu"></div>
    <div class="abs topbar__platform">Streamly</div>
    <div class="abs topbar__search">
      <div class="abs topbar__search-btn"></div>
    </div>
    <svg class="abs topbar__icons" width="80" height="20" viewBox="0 0 80 20">
      <path d="M8 12 V5 M5 8 L8 5 L11 8 M5 13 H11" stroke="#777" stroke-width="1.4" fill="none"/>
      <path d="M30 12 H38 L37 10.5 V8 A3 3 0 0 0 31 8 V10.5 Z M33 13 H35" stroke="#777" stroke-width="1.2" fill="#777"/>
      <circle cx="63" cy="8" r="8" fill="#333"/>
    </svg>
  </header>

  <section class="channel-art">
    <svg class="abs" width="928" height="158" viewBox="0 0 928 158">
      <defs>
        <linearGradient id="study-tones" x1="0" y1="0" x2="1" y2="1">
          <stop offset="0" stop-color="#8a6a4f"/>
          <stop offset="0.55" stop-color="#5a4536"/>
          <stop offset="1" stop-color="#c7b6a4"/>
        </linearGradient>
      </defs>
      <path d="M166 20 A40 60 0 0 1 166 140 Z" fill="var(--orange)"/>
      <path d="M166 9 A47 71 0 0 1 166 151" fill="none" stroke="var(--grey-line)" stroke-width="1.5"/>
      <g role="img" aria-label="Photo: two students studying together at a laptop in a library">
        <circle cx="460" cy="80" r="74" fill="url(#study-tones)"/>
      </g>
      <circle cx="460" cy="80" r="74" fill="none" stroke="var(--orange)" stroke-width="3"/>
      <path d="M755 26 A17 54 0 0 0 755 134 Z" fill="var(--orange)"/>
      <path d="M755 16 A30 64 0 0 0 755 144" fill="none" stroke="var(--grey-line)" stroke-width="1.5"/>
    </svg>
    <p class="channel-art__values">Our core values are<br>personalisation,<br>family and success.</p>
    <div class="brand">
      <div class="brand__mark"></div>
      <div class="brand__name"><strong>Lernwerk</strong><span>Bildungsinstitut</span></div>
    </div>
  </section>

  <section class="channel-head">
    <div class="abs channel-head__avatar"></div>
    <div class="abs channel-head__name">Lernwerk Bildungsinstitut</div>
    <div class="abs channel-head__subs">500.000 subscribers</div>
    <div class="abs channel-head__subscribe">SUBSCRIBE</div>
    <nav class="abs tabs">
      <span class="tabs__item tabs__item--active" style="left:17px">HOME</span>
      <span class="tabs__item" style="left:72px">VIDEOS</span>
      <span class="tabs__item" style="left:129px">PLAYLISTS</span>
      <span class="tabs__item" style="left:193px">CHANNELS</span>
      <span class="tabs__item" style="left:257px">DISCUSSION</span>
      <span class="tabs__item" style="left:330px">ABOUT</span>
      <svg class="tabs__item" style="left:388px; top:-1px" width="9" height="9" viewBox="0 0 9 9">
        <circle cx="3.6" cy="3.6" r="2.6" fill="none" stroke="#777" stroke-width="1"/>
        <path d="M5.5 5.5 L8 8" stroke="#777" stroke-width="1"/>
      </svg>
    </nav>
    <div class="abs tabs__underline" style="left:127px; top:73px"></div>
  </section>

  <div class="abs featured-cover">
    <div class="video-cover">
      <svg class="video-cover__art" width="829" height="466" viewBox="0 0 829 466">
        <defs>
          <linearGradient id="library-tones-small" x1="0" y1="0" x2="1" y2="1">
            <stop offset="0" stop-color="var(--photo-dark)"/>
            <stop offset="0.5" stop-color="var(--photo-mid)"/>
            <stop offset="1" stop-color="var(--photo-light)"/>
          </linearGradient>
        </defs>
        <g role="img" aria-label="Photo: two pupils studying with a laptop and books in a library">
          <path d="M568 0 C440 70 360 160 360 240 C360 330 410 420 483 466 L829 466 L829 0 Z" fill="url(#library-tones-small)"/>
        </g>
        <path d="M568 0 C440 70 360 160 360 240 C360 330 410 420 483 466" fill="none" stroke="var(--black)" stroke-width="5"/>
      </svg>
      <div class="brand">
        <div class="brand__mark"></div>
        <div class="brand__name"><strong>Lernwerk</strong><span>Bildungsinstitut</span></div>
      </div>
      <p class="video-cover__tagline">We are an online platform for pupils who provide<br>group courses and on demand individual tutroing lessons.</p>
      <div class="video-cover__stripe video-cover__stripe--upper"></div>
      <div class="video-cover__stripe video-cover__stripe--lower"></div>
    </div>
  </div>

  <div class="abs featured-info">
    <p class="featured-info__title">Editable Video Name - Exemple</p>
    <p class="featured-info__meta">500.000 views • 1 day ago</p>
    <p class="featured-info__body">Lorem ipsum dolor sit amet, consectetur adipisicing elit, sed do eiusmod tempor incididunt ut labore et dolore magna aliqua. Ut enim ad minim veniam, quis nostrud exercitation ullamco laboris nisi ut aliquip ex ea commodo consequat. Duis aute irure dolor in reprehenderit in voluptate velit esse cillum dolore eu fugiat nulla pariatur. Excepteur sint occaecat cupidatat non proident, sunt in culpa qui officia deserunt mollit anim id est laborum.</p>
    <div class="featured-info__rule"></div>
    <p class="featured-info__body" style="margin-top:0">Sed ut perspiciatis unde omnis iste natus error sit voluptatem accusantium doloremque laudantium, totam rem aperiam, eaque ipsa quae ab illo inventore veritatis et quasi architecto beatae vitae dicta sunt explicabo. Nemo enim ipsam</p>
  </div>

  <div class="abs section-rule"></div>
  <div class="abs uploads-label">UPLOADS</div>
  <div class="abs uploads-play">PLAY ALL</div>

  <div class="abs uploads">
    <div class="upload"><div class="upload__thumb"><span class="upload__badge"></span><span class="upload__highlight">THUMBNAIL HIGHLIGHT</span><span class="upload__sub"></span></div><p class="upload__title">Editable Video Name - Exemple</p><p class="upload__meta">100.000 views • 2 days ago</p></div>
    <div class="upload"><div class="upload__thumb"><span class="upload__badge"></span><span class="upload__highlight">THUMBNAIL HIGHLIGHT</span><span class="upload__sub"></span></div><p class="upload__title">Editable Video Name - Exemple</p><p class="upload__meta">200.000 views • 3 days ago</p></div>
    <div class="upload"><div class="upload__thumb"><span class="upload__badge"></span><span class="upload__highlight">THUMBNAIL HIGHLIGHT</span><span class="upload__sub"></span></div><p class="upload__title">Editable Video Name - Exemple</p><p class="upload__meta">100.000 views • 4 days ago</p></div>
    <div class="upload"><div class="upload__thumb"><span class="upload__badge"></span><span class="upload__highlight">THUMBNAIL HIGHLIGHT</span><span class="upload__sub"></span></div><p class="upload__title">Editable Video Name - Exemple</p><p class="upload__meta">200.000 views • 5 days ago</p></div>
    <div class="upload"><div class="upload__thumb"><span class="upload__badge"></span><span class="upload__highlight">THUMBNAIL HIGHLIGHT</span><span class="upload__sub"></span></div><p class="upload__title">Editable Video Name - Exemple</p><p class="upload__meta">100.000 views • 6 days ago</p></div>
    <div class="upload"><div class="upload__thumb"><span class="upload__badge"></span><span class="upload__highlight">THUMBNAIL HIGHLIGHT</span><span class="upload__sub"></span></div><p class="upload__title">Editable Video Name - Exemple</p><p class="upload__meta">100.000 views • 7 days ago</p></div>
  </div>
</section>

<section class="stage">
  <div class="video-cover">
    <svg class="video-cover__art" width="829" height="466" viewBox="0 0 829 466">
      <defs>
        <linearGradient id="library-tones" x1="0" y1="0" x2="1" y2="1">
          <stop offset="0" stop-color="var(--photo-dark)"/>
          <stop offset="0.5" stop-color="var(--photo-mid)"/>
          <stop offset="1" stop-color="var(--photo-light)"/>
        </linearGradient>
      </defs>
      <g role="img" aria-label="Photo: two pupils studying with a laptop and books in a library">
        <path d="M568 0 C440 70 360 160 360 240 C360 330 410 420 483 466 L829 466 L829 0 Z" fill="url(#library-tones)"/>
      </g>
      <path d="M568 0 C440 70 360 160 360 240 C360 330 410 420 483 466" fill="none" stroke="var(--black)" stroke-width="5"/>
    </svg>
    <div class="brand">
      <div class="brand__mark"></div>
      <div class="brand__name"><strong>Lernwerk</strong><span>Bildungsinstitut</span></div>
    </div>
    <p class="video-cover__tagline">We are an online platform for pupils who provide<br>group courses and on demand individual tutroing lessons.</p>
    <div class="video-cover__stripe video-cover__stripe--upper"></div>
    <div class="video-cover__stripe video-cover__stripe--lower"></div>
  </div>
</section>

</body>
</html>
```